Breezy Trinkets Handcrafted Copper Jewelry

I make handcrafted copper bracelets and cuffs.
I need a banner made (2' 1/2" x 10')
I attached the logo (I would like that sketch to be purple)
Company name: Breezy Trinkets (in a "sassy" font)
Tag line: Wear your Breeze
Designer/Creator: Norma Tillery
481.307.6624
FB: www.facebook.com/breezytrinkets.example
shop.breezytrinkets.example
I'd like the background to be white. I'm not sure what I'm looking for as far as the look or if I should add any pics of the copper jewelry that I make. I'm totally up for suggestions. I'm very eager to see how creative you can be.
Many thanks.
Jewelry

```html
<!DOCTYPE html>
<html lang="en">
<head>
<meta charset="utf-8">
<title>Breezy Trinkets Banner</title>
<link rel="stylesheet" href="https://fonts.googleapis.com/css2?family=Dancing+Script:wght@700&family=Quicksand:wght@400;500&display=swap">
<style>
  :root {
    --stage: #f3efee;
    --pink-light: #fbd6ea;
    --pink-mid: #f6b9da;
    --pink-deep: #f0a3cc;
    --purple: #6a3d9a;
    --purple-soft: #7c52ab;
    --shadow-pink: rgba(255, 255, 255, 0.75);
  }
  html, body {
    margin: 0;
    padding: 0;
    width: 1200px;
    height: 1000px;
    overflow: hidden;
    background: var(--stage);
  }
  .canvas {
    position: relative;
    width: 1200px;
    height: 1000px;
  }
  .banner {
    position: absolute;
    left: 80px;
    top: 370px;
    width: 1040px;
    height: 260px;
    overflow: hidden;
    background:
      radial-gradient(circle at 12% 70%, var(--pink-deep) 0 14%, transparent 15%),
      radial-gradient(circle at 40% 20%, var(--pink-mid) 0 16%, transparent 17%),
      radial-gradient(circle at 75% 85%, var(--pink-deep) 0 15%, transparent 16%),
      radial-gradient(circle at 92% 25%, var(--pink-mid) 0 14%, transparent 15%),
      linear-gradient(180deg, var(--pink-light) 0%, var(--pink-mid) 100%);
    box-shadow: 0 1px 3px rgba(0,0,0,0.2);
  }
  .brand-name {
    position: absolute;
    left: 50px;
    top: 38px;
    margin: 0;
    font-family: "Dancing Script", cursive;
    font-weight: 700;
    font-size: 82px;
    line-height: 1;
    color: var(--purple);
    text-shadow: 2px 2px 0 var(--shadow-pink);
    white-space: nowrap;
  }
  .creator {
    position: absolute;
    left: 762px;
    top: 92px;
    font-family: "Dancing Script", cursive;
    font-weight: 700;
    font-size: 28px;
    color: var(--purple);
    white-space: nowrap;
  }
  .tagline {
    position: absolute;
    left: 436px;
    top: 145px;
    margin: 0;
    font-family: "Dancing Script", cursive;
    font-weight: 700;
    font-size: 50px;
    line-height: 1;
    color: var(--purple);
    text-shadow: 2px 3px 2px rgba(80, 30, 110, 0.35);
    white-space: nowrap;
  }
  .figure-sketch {
    position: absolute;
    left: 635px;
    top: 8px;
    width: 115px;
    height: 248px;
    border-radius: 40px 40px 10px 10px;
    background: linear-gradient(180deg, rgba(160,110,200,0.35), rgba(130,80,180,0.2));
  }
  .contact-row {
    position: absolute;
    left: 0;
    top: 212px;
    width: 1040px;
    height: 28px;
    font-family: "Quicksand", sans-serif;
    font-weight: 500;
    font-size: 19px;
    color: var(--purple-soft);
  }
  .contact {
    position: absolute;
    top: 0;
    line-height: 28px;
    white-space: nowrap;
  }
  .contact-phone { left: 75px; }
  .contact-social { left: 321px; display: flex; align-items: center; gap: 5px; }
  .contact-social .dot {
    width: 26px;
    height: 26px;
    border-radius: 50%;
    background: var(--purple);
  }
  .contact-shop { right: 32px; }
</style>
</head>
<body>
<div class="canvas">
  <section class="banner">
    <h1 class="brand-name">Breezy Trinkets</h1>
    <div class="figure-sketch" role="img" aria-label="Purple line sketch of a woman in a flowing strapless dress and boots"></div>
    <span class="creator">by Norma Tillery</span>
    <p class="tagline">Wear your Breeze</p>
    <div class="contact-row">
      <span class="contact contact-phone">481.307.6624</span>
      <span class="contact contact-social"><span class="dot"></span>breezytrinkets.example</span>
      <span class="contact contact-shop">www.shop.breezytrinkets.example</span>
    </div>
  </section>
</div>
</body>
</html>
```